依頼詳細
建設業界では、まだ段階の世代で古き良き
日本というカテゴリが強く残っている現状ですが
大手スーパーゼネコンのように、現代の最先端のユーモアさも取り入れ
他の建設業界とは、一風変わった特徴ある名刺を作成したいと
考えて応募しました。
記載項目
株式会社 DAVRO
代表取締役 高野 典久
希望イメージ
シンプル 複雑
単色 カラフル
暗い 明るい
日常 高級
遊び心 厳粛
未来的 伝統的
女性的 男性的
希望する色
オレンジ
納品ファイル
• 高解像度JPG (.jpg)
• フォトショップ形式 (.psd)
補足説明
当社のロゴのdataを追加しました。

ですが必ずしもロゴを記載したいというわけではございません
自分自身は趣味でヨーロッパなどの歴史ある建造物などを
見に足を運ぶなどもしております。(^^)
■ 選んだ理由

横のデザイン構成・全体的なバランス
がとても気に入り決断致しました。

■ 提案者全員のお礼・コメント

この度は皆様方に
様々なご提案、ご参加いただき
誠にお礼を申し上げる次第です。

ありがとうございます。

```html
<!DOCTYPE html>
<html lang="ja">
<head>
<meta charset="utf-8">
<title>DAVRO 名刺</title>
<link rel="stylesheet" href="https://fonts.googleapis.com/css2?family=Noto+Sans+JP:wght@400;500;700&family=Noto+Serif:ital@1&display=swap">
<style>
  :root {
    --canvas-bg: #efe6d6;
    --cloth-light: #e2c896;
    --cloth-mid: #d3b37c;
    --cloth-dark: #c09c62;
    --torn-dark: #5a3b22;
    --torn-deep: #3f2716;
    --torn-edge: #f1e7d4;
    --ink: #2e241b;
    --ink-soft: #45382b;
    --brand-orange: #e8801e;
    --roman-ink: #f7f1e6;
  }
  * { margin: 0; padding: 0; box-sizing: border-box; }
  html, body { width: 726px; height: 1200px; overflow: hidden; background: var(--canvas-bg); }
  .card {
    position: relative;
    width: 726px;
    height: 1200px;
    overflow: hidden;
    font-family: "Noto Sans JP", sans-serif;
    color: var(--ink);
  }
  .cloth-texture {
    position: absolute; inset: 0;
    background: linear-gradient(160deg, var(--cloth-light) 0%, var(--cloth-mid) 55%, var(--cloth-dark) 100%);
  }
  .torn-patch { position: absolute; left: 0; top: 0; width: 726px; height: 1200px; }
  .brand {
    position: absolute;
    left: 404px; top: 412px;
    display: flex; align-items: center; gap: 12px;
  }
  .brand-dot { width: 30px; height: 30px; border-radius: 50%; background: var(--brand-orange); }
  .brand-name {
    font-weight: 700; font-size: 42px; letter-spacing: 2px;
    color: var(--brand-orange); line-height: 1;
  }
  .identity { position: absolute; left: 218px; top: 505px; }
  .role { font-size: 34px; font-weight: 500; letter-spacing: 4px; line-height: 1.3; margin-left: 8px; }
  .person-name { margin-top: 14px; font-size: 62px; font-weight: 500; letter-spacing: 8px; line-height: 1.15; }
  .person-roman {
    margin-top: 2px;
    font-family: "Noto Serif", serif; font-style: italic;
    font-size: 28px; letter-spacing: 1px;
    color: var(--roman-ink);
    text-shadow: 0 0 2px var(--ink-soft);
  }
  .contact { position: absolute; left: 213px; top: 880px; color: var(--ink-soft); }
  .company { font-size: 26px; font-weight: 500; margin-bottom: 8px; }
  .contact-line { font-size: 21px; line-height: 40px; white-space: nowrap; letter-spacing: 0.3px; }
  .contact-line.with-icon { display: flex; align-items: center; gap: 10px; }
  .contact-icon { width: 28px; height: 28px; flex: none; }
</style>
</head>
<body>
<main class="card">
  <div class="cloth-texture" role="img" aria-label="Woven burlap cloth texture in warm tan"></div>

  <svg class="torn-patch" viewBox="0 0 726 1200" role="img" aria-label="Torn opening revealing dark brown woven fabric">
    <path d="M0 0 H385 C365 80 315 140 265 200 C295 260 315 330 265 400 C215 455 195 515 220 570 C240 640 235 700 210 760 C190 820 185 880 160 945 C130 1010 90 1085 0 1150 Z"
          fill="var(--torn-edge)"/>
    <path d="M0 0 H362 C343 78 295 136 246 198 C275 258 292 328 245 396 C198 452 178 512 200 568 C218 636 214 698 190 756 C170 816 166 876 142 938 C114 1000 76 1070 0 1128 Z"
          fill="var(--torn-dark)"/>
    <path d="M0 0 H220 C190 160 140 340 80 580 C55 700 25 820 0 900 Z" fill="var(--torn-deep)" opacity="0.35"/>
  </svg>

  <div class="brand">
    <span class="brand-dot"></span>
    <span class="brand-name">DAVRO</span>
  </div>

  <section class="identity">
    <p class="role">代表取締役</p>
    <h1 class="person-name">高野 典久</h1>
    <p class="person-roman">Takano Norihisa</p>
  </section>

  <section class="contact">
    <p class="company">株式会社 DAVRO</p>
    <p class="contact-line">〒100-0021</p>
    <p class="contact-line">東京都千代田区緑葉町 5-2-8</p>
    <p class="contact-line">TEL 03-5820-4417 _ FAX 03-5820-4418</p>
    <p class="contact-line with-icon">
      <svg class="contact-icon" viewBox="0 0 28 28" aria-hidden="true">
        <rect x="7" y="2" width="14" height="24" rx="3" fill="var(--ink-soft)"/>
        <rect x="9.5" y="5" width="9" height="14" fill="var(--cloth-light)"/>
        <circle cx="14" cy="22.5" r="1.6" fill="var(--cloth-light)"/>
      </svg>
      090-6213-7754
    </p>
    <p class="contact-line with-icon">
      <svg class="contact-icon" viewBox="0 0 28 28" aria-hidden="true">
        <rect x="2" y="6" width="24" height="16" rx="2" fill="none" stroke="var(--ink-soft)" stroke-width="2.2"/>
        <path d="M3 7 L14 16 L25 7" fill="none" stroke="var(--ink-soft)" stroke-width="2.2"/>
      </svg>
      info@davro-kensetsu.jp
    </p>
  </section>
</main>
</body>
</html>
```